Commercial Loan Originator Business Card (CHANGE COLORS SCHEME)

CHANGE COLOR SCHEME - SAME DESIGN

Name Marissa Lantham
Title Commercial Loan Originator
Office (800) 641-2905 x68
Direct (240) 617-2435
Email brightleaf4you@mailpost.example

Name Derek Fallow
Office (800) 641-2905 x70
Direct (410) 932-1864
Email d.falthebroker@mailpost.example

Name Gordon Wexley
Office (800) 641-2905 x71
Direct (215) 346-2081
Email g.wexley37@mailpost.example

Name Lyn Moreau
Office (800) 641-2905 x
Direct (202) 458-1937
Email lmoreau64@mailpost.example

Name Nadia Strand
Office (800) 641-2905 x72
Direct (240) 871-5246
Email qrzhomelending@mailpost.example

```html
<!DOCTYPE html>
<html lang="en">
<head>
<meta charset="utf-8">
<title>Marissa Lantham – Commercial Loan Originator</title>
<link rel="stylesheet" href="https://fonts.googleapis.com/css2?family=Bodoni+Moda:wght@400;500&family=Poppins:wght@400;500&display=swap">
<style>
  :root {
    --page-bg: #e9ebeb;
    --card-bg: #ffffff;
    --accent: #12808a;
    --accent-deep: #0c5f68;
    --accent-soft: #7fc3c4;
    --ink: #1c2a36;
    --rule: #9aa6aa;
    --panel-grey: #e8ecec;
  }
  * { box-sizing: border-box; margin: 0; padding: 0; }
  html, body {
    width: 1200px; height: 1200px; overflow: hidden;
    background: var(--page-bg);
  }
  .card {
    position: absolute; left: 40px; top: 280px;
    width: 1120px; height: 639px;
    background: var(--card-bg);
    overflow: hidden;
  }
  .portrait-art { position: absolute; left: 0; top: 0; }
  .name {
    position: absolute; left: 0; top: 0;
    font-family: "Bodoni Moda", "Didot", serif;
    font-weight: 400;
  }
  .name-svg { display: block; }
  .name-initial { fill: var(--accent); font-size: 132px; font-weight: 500; }
  .name-first { fill: var(--accent); font-size: 84px; }
  .name-last { fill: var(--ink); font-size: 96px; font-weight: 500; }
  .title {
    position: absolute; left: 548px; width: 482px; top: 274px;
    text-align: right; padding-right: 14px;
    font-family: "Poppins", "Helvetica", sans-serif;
    font-size: 25px; font-weight: 500; color: var(--ink);
    letter-spacing: 0.4px; white-space: nowrap;
  }
  .rule {
    position: absolute; left: 548px; top: 341px;
    width: 482px; height: 1px; background: var(--rule);
  }
  .contact-icons { position: absolute; left: 726px; top: 377px; }
  .contact-list {
    position: absolute; left: 548px; width: 482px; top: 424px;
    list-style: none; text-align: center;
    font-family: "Poppins", "Helvetica", sans-serif;
    font-size: 23px; color: var(--ink); letter-spacing: 0.3px;
  }
  .contact-list li { height: 46px; line-height: 40px; white-space: nowrap; }
  .contact-list .email { margin-top: 4px; }
</style>
</head>
<body>
  <main class="card">
    <svg class="portrait-art" width="600" height="639" viewBox="0 0 600 639">
      <defs>
        <linearGradient id="portraitFill" x1="0" y1="0" x2="0" y2="1">
          <stop offset="0" stop-color="#e8ecec"/>
          <stop offset="0.45" stop-color="#b9a6a0"/>
          <stop offset="0.65" stop-color="#3f9ea4"/>
          <stop offset="1" stop-color="#2a8f96"/>
        </linearGradient>
        <radialGradient id="dropShadow" cx="0.5" cy="0.5" r="0.5">
          <stop offset="0" stop-color="#06363b" stop-opacity="0.55"/>
          <stop offset="1" stop-color="#06363b" stop-opacity="0"/>
        </radialGradient>
      </defs>
      <circle class="accent-disc" cx="291" cy="680" r="196" fill="var(--accent-deep)"/>
      <ellipse cx="291" cy="580" rx="140" ry="12" fill="url(#dropShadow)"/>
      <path class="portrait-ring" d="M102 396 A189 189 0 0 0 480 396" fill="none" stroke="#ffffff" stroke-width="12"/>
      <path class="portrait-photo" role="img" aria-label="Portrait photo of the loan originator smiling"
            d="M102 0 H479 V396 A189 189 0 0 1 102 396 Z" fill="url(#portraitFill)"/>
    </svg>

    <h1 class="name" aria-label="Marissa Lantham">
      <svg class="name-svg" width="1120" height="270" viewBox="0 0 1120 270" aria-hidden="true">
        <text class="name-initial" x="548" y="180">M</text>
        <text class="name-first" x="676" y="180" textLength="262" lengthAdjust="spacingAndGlyphs">arissa</text>
        <text class="name-last" x="658" y="254" textLength="368" lengthAdjust="spacingAndGlyphs">Lantham</text>
      </svg>
    </h1>
    <p class="title">Commercial Loan Originator</p>
    <div class="rule"></div>

    <svg class="contact-icons" width="130" height="38" viewBox="0 0 130 38" aria-hidden="true">
      <g fill="var(--accent)">
        <circle cx="18" cy="19" r="18"/>
        <circle cx="63" cy="19" r="18"/>
        <circle cx="107" cy="19" r="18"/>
      </g>
      <g fill="#ffffff">
        <path d="M8 15 q10 -7 20 0 v3 h-5 v-2 q-5 -2 -10 0 v2 h-5 z"/>
        <rect x="11" y="19" width="14" height="9" rx="2"/>
        <path d="M56 11 l4 -1 l2 5 l-2.5 2 q2 5 6 7.5 l2 -2.5 l5 2 l-1 4 q-2 2 -5 1 q-9 -4 -12 -13 q-0.5 -3 1.5 -5z"/>
        <rect x="97" y="12" width="20" height="14" rx="1.5"/>
      </g>
      <path d="M97.5 13 l9.5 7.5 l9.5 -7.5 M97.5 25.5 l7 -6 M116.5 25.5 l-7 -6" fill="none" stroke="var(--accent)" stroke-width="1.4"/>
    </svg>

    <ul class="contact-list">
      <li class="office">(800) 641-2905 x68</li>
      <li class="direct">(240) 617-2435</li>
      <li class="email">brightleaf4you@mailpost.example</li>
    </ul>
  </main>
</body>
</html>
```